Tallwater Marketing Business Card

Business card using new logo for marketing consulting company based in Silicon Valley. Limited information on card now (name, phone number, email, website), but room to add mailing address later.

```html
<!DOCTYPE html>
<html lang="en">
<head>
<meta charset="utf-8">
<title>Tallwater Marketing Business Card</title>
<link rel="stylesheet" href="https://fonts.googleapis.com/css2?family=Open+Sans:wght@400;600&display=swap">
<style>
  :root {
    --backdrop: #988676;
    --paper: #ffffff;
    --navy: #1b325e;
    --sky: #29bff0;
    --sky-soft: #6ccbf2;
    --label: #ffffff;
  }
  * { margin: 0; padding: 0; box-sizing: border-box; }
  html, body { width: 1200px; height: 1000px; overflow: hidden; }
  body {
    background: var(--backdrop);
    font-family: "Open Sans", Arial, sans-serif;
    position: relative;
  }
  .side-label {
    position: absolute;
    color: var(--label);
    font-weight: 400;
    line-height: 1;
  }
  .side-label--front { left: 720px; top: 172px; font-size: 60px; }
  .side-label--back { left: 118px; top: 660px; font-size: 80px; }

  .card { position: absolute; background: var(--paper); overflow: hidden; }
  .card--front { left: 58px; top: 62px; width: 551px; height: 321px; }
  .card--back { left: 365px; top: 460px; width: 783px; height: 458px; }

  .brand {
    position: absolute;
    display: flex;
    flex-direction: column;
    align-items: center;
    color: var(--sky);
    font-weight: 400;
    line-height: 1;
  }
  .brand__dot {
    border-radius: 50%;
    background: var(--sky);
  }
  .brand__name { letter-spacing: 1px; }
  .brand__field { letter-spacing: 5px; margin-top: 8px; }

  .card--front .brand { left: 0; width: 551px; top: 74px; }
  .card--front .brand__dot { width: 74px; height: 74px; margin-bottom: 36px; }
  .card--front .brand__name { font-size: 38px; }
  .card--front .brand__field { font-size: 17px; }

  .card--back .brand { left: 8px; width: 330px; top: 118px; }
  .card--back .brand__dot { width: 78px; height: 78px; margin-bottom: 58px; }
  .card--back .brand__name { font-size: 43px; }
  .card--back .brand__field { font-size: 18px; }

  .card__panel { position: absolute; inset: 0; width: 783px; height: 458px; }

  .contact { position: absolute; left: 450px; top: 0; color: var(--paper); }
  .contact__name { position: absolute; top: 88px; font-size: 33.5px; white-space: nowrap; }
  .contact__phone {
    position: absolute; top: 166px; font-size: 48px; font-weight: 600;
    color: var(--sky-soft); white-space: nowrap; letter-spacing: 0.5px;
  }
  .contact__rule {
    position: absolute; left: 192px; top: 230px;
    width: 116px; height: 3px; background: var(--sky);
  }
  .contact__web { position: absolute; left: 7px; top: 273px; font-size: 28px; white-space: nowrap; }
  .contact__email { position: absolute; left: 6px; top: 323px; font-size: 20.5px; white-space: nowrap; }
</style>
</head>
<body>
  <section class="card card--front">
    <div class="brand">
      <div class="brand__dot"></div>
      <div class="brand__name">TALLWATER</div>
      <div class="brand__field">MARKETING</div>
    </div>
  </section>
  <div class="side-label side-label--front">Front</div>

  <div class="side-label side-label--back">Back</div>
  <section class="card card--back">
    <svg class="card__panel" viewBox="0 0 783 458" aria-hidden="true">
      <path d="M320 0 Q500 229 335 458 L783 458 L783 0 Z" fill="var(--navy)"/>
      <path d="M320 0 Q500 229 335 458" fill="none" stroke="var(--sky-soft)" stroke-width="4" opacity="0.7"/>
    </svg>
    <div class="brand">
      <div class="brand__dot"></div>
      <div class="brand__name">TALLWATER</div>
      <div class="brand__field">MARKETING</div>
    </div>
    <div class="contact">
      <div class="contact__name">Your Name Here</div>
      <div class="contact__phone">1-800-000000</div>
      <div class="contact__rule"></div>
      <div class="contact__web">www.yourdomain.com</div>
      <div class="contact__email">your.email@yourdomain.com</div>
    </div>
  </section>
</body>
</html>
```